Vyrella Motion Design
Would like the design to go over the page in a way that can type over it.
We are a personal training and small group studio
Want it to be professional and classy
Reason: Asked for some modifications on a few designs, want to give the designers time to do this
Target Market(s)
All age groups, sports professionals as well as business professionals, families
Industry/Entity Type
Training
Requirements
Must have
- Must have Vyrella Motion Studio
Mira Pendleby
314 Calloway Street
Marbeck Vale
Eastholm Territory 7204
Phone: 0497318260
Nice to have
- Professional classy fonts
Colour
Should not have
- Clip art
Balloons

```html
<!DOCTYPE html>
<html lang="en">
<head>
<meta charset="utf-8">
<title>Vyrella Motion Studio – Letterhead</title>
<link rel="stylesheet" href="https://fonts.googleapis.com/css2?family=Open+Sans:wght@400;700;800&display=swap">
<style>
  :root {
    --paper: #ffffff;
    --brand-blue: #0b3f9e;
    --brand-blue-deep: #0a2f8a;
    --brand-cyan: #1fc3f3;
    --brand-orange: #ff6a0c;
    --text-dark: #333333;
    --label-cyan: #1aa3e0;
  }
  * { margin: 0; padding: 0; box-sizing: border-box; }
  html, body {
    width: 919px;
    height: 1200px;
    overflow: hidden;
    background: var(--paper);
    font-family: "Open Sans", Arial, sans-serif;
  }
  .letterhead {
    position: relative;
    width: 919px;
    height: 1200px;
    background: var(--paper);
    overflow: hidden;
  }
  .header-swoosh {
    position: absolute;
    top: 0;
    left: 0;
    width: 919px;
    height: 280px;
  }
  .sender {
    position: absolute;
    top: 56px;
    right: 53px;
    text-align: right;
    color: #ffffff;
    font-weight: 700;
    line-height: 26px;
  }
  .sender-company { font-size: 15px; }
  .sender-name { font-size: 14px; }
  .brand {
    position: absolute;
    top: 150px;
    left: 50px;
    display: flex;
    align-items: center;
    gap: 12px;
  }
  .brand-dot {
    width: 34px;
    height: 34px;
    border-radius: 50%;
    background: var(--brand-orange);
  }
  .brand-name {
    font-size: 28px;
    font-weight: 800;
    color: var(--brand-blue);
    letter-spacing: -0.5px;
  }
  .footer {
    position: absolute;
    left: 0;
    right: 0;
    top: 1138px;
    text-align: center;
    font-size: 13.5px;
    color: var(--text-dark);
    line-height: 22px;
  }
  .footer-label {
    font-weight: 700;
    color: var(--label-cyan);
  }
  .footer-gap { display: inline-block; width: 14px; }
</style>
</head>
<body>
<main class="letterhead">
  <svg class="header-swoosh" viewBox="0 0 919 280" aria-hidden="true">
    <defs>
      <radialGradient id="bandGlow" cx="390" cy="0" r="380" gradientUnits="userSpaceOnUse">
        <stop offset="0" stop-color="#1fc3f3"/>
        <stop offset="0.55" stop-color="#0b3f9e"/>
        <stop offset="1" stop-color="#0a2f8a"/>
      </radialGradient>
    </defs>
    <path class="band-blue" d="M0,0 H919 V230 C650,100 300,25 0,42 Z" fill="url(#bandGlow)"/>
    <path class="band-orange" d="M0,52 C300,36 650,112 919,246 V278 C650,138 300,48 0,62 Z" fill="#ff6a0c"/>
  </svg>

  <div class="sender">
    <div class="sender-company">Vyrella Motion Studio</div>
    <div class="sender-name">Mira Pendleby</div>
  </div>

  <div class="brand">
    <span class="brand-dot"></span>
    <span class="brand-name">Vyrella Motion Studio</span>
  </div>

  <footer class="footer">
    <div class="footer-address">314 Calloway Street Marbeck Vale Eastholm Territory 7204</div>
    <div class="footer-contact">
      <span class="footer-label">Phone</span> : 0497318260<span class="footer-gap"></span><span class="footer-label">Email</span> : info@vyrellamotion.com
    </div>
  </footer>
</main>
</body>
</html>
```